magcian / mentalist needs flyer desined to send potentisl clients

I need a design that's contemporary, sharp, fun, and professional that will get the attention of whoever receives the flyer very quickly. This is for a tri-fold flyer design.

I've been performing magic for over 40 years. I've performed close-up,
parlor, and stage shows. I've been an Master of Ceremonies, Key Note
Speaker (using magic during presentations to help build on a point or
topic, while keeping the audience entertained and educated on the topic or
topics the client has asked me to focus). I've worked trade shows and
sales training incorporating magic as well. I did private shows in Las
Vegas and L.A. back in the late 90's as well.

I do have website / wesleytorvandmagic.example for your to check out.

Target Market(s)

The target audience is corporation Event Planners, Marketing and Sales
managers, casino & hotel entertainment directors, as well as private
businesses looking for unique entertainment options.

Industry/Entity Type

Entertainment Industry

Logo Text

Here are a couple of ideas: your mind is my playground, neural entertainer, professor of mysteries, master of your mind

Requirements
Must have
• I like the black and white look (I think it looks nice, but open to other
• ideas and creativity. Being I'm a magician and mentalist, I'd like for
• both venues to be conveyed somehow. My magic is clean and corporate and family friendly.
Nice to have
• I do have website / wesleytorvandmagic.example for your to check out.
• My current business card is attached for review. I'll also attach photos
• I'd like to share, but was unable when I last attempted do sign up. Some
• of the files were too big and I'm not savvy enough to make them smaller,
• but think there might be some potential with a couple.
Should not have
• cartoons or cartoonish graphics. no rabbits, doves, magicians, wands, or top hats.

```html
<!DOCTYPE html>
<html lang="en">
<head>
<meta charset="utf-8">
<title>Wesley Torvand Magic – Tri-fold Flyer</title>
<link href="https://fonts.googleapis.com/css2?family=Anton&family=Lato:wght@300;400;700&family=Great+Vibes&family=Cinzel:wght@700&display=swap" rel="stylesheet">
<style>
  :root {
    --page-bg: #efebe4;
    --panel-gray: #6a6a6d;
    --panel-gray-light: #7a7a7d;
    --panel-black: #0b0b0d;
    --panel-navy: #15151f;
    --ring: #8a8a8f;
    --label-bg: #ffffff;
    --label-ink: #0b0b0d;
    --text-strong: #ffffff;
    --text-soft: #c9c9cf;
    --text-dim: #a9a9b2;
  }
  * { box-sizing: border-box; margin: 0; padding: 0; }
  html, body { width: 1200px; height: 1200px; overflow: hidden; }
  body { background: var(--page-bg); position: relative; font-family: "Lato", sans-serif; }

  .flyer {
    position: absolute; left: 152px; top: 20px;
    width: 896px; height: 1160px; overflow: hidden;
    background: var(--panel-gray);
    box-shadow: 0 10px 30px rgba(0,0,0,.35);
  }
  .flyer-shapes { position: absolute; inset: 0; }

  .section-label {
    position: absolute; background: var(--label-bg); color: var(--label-ink);
    font-family: "Anton", sans-serif; font-size: 20px; line-height: 1;
    padding: 4px 6px 3px; border: 2px solid #cfcfcf; letter-spacing: .2px;
  }

  .photo {
    position: absolute; border-radius: 50%;
    border: 8px solid var(--ring);
    box-shadow: 0 0 18px rgba(255,255,255,.25);
  }
  .photo--warm { background: radial-gradient(circle at 45% 40%, #b98f64 0%, #7a5634 45%, #2c211a 100%); }
  .photo--warm-red { background: radial-gradient(circle at 50% 70%, #a33a30 0%, #8c6a4c 35%, #3a2c22 100%); }
  .photo--mono { background: radial-gradient(circle at 40% 45%, #9a9a9a 0%, #4d4d4d 50%, #141414 100%); }
  .photo--stage { background: radial-gradient(circle at 50% 45%, #5b4a45 0%, #2a2230 55%, #12121c 100%); }

  .hero-photo {
    position: absolute; left: 610px; top: 240px; width: 286px; height: 820px;
    background: radial-gradient(ellipse at 60% 35%, #8a6d5c 0%, #3b2c2a 40%, #1a1620 75%, rgba(21,21,31,0) 100%);
  }

  .copy { position: absolute; width: 268px; color: var(--text-soft); font-weight: 300; font-size: 10.6px; line-height: 1.4; }
  .copy p { margin-bottom: 10px; }
  .copy .lead { color: var(--text-strong); font-weight: 400; font-size: 11.3px; }
  .copy .subhead { color: var(--text-strong); font-weight: 400; font-size: 11px; }
  .copy strong { color: var(--text-strong); font-weight: 400; }

  .brand {
    position: absolute; left: 628px; top: 60px; width: 250px;
    display: flex; align-items: center; gap: 10px;
    font-family: "Lato", sans-serif; font-weight: 400; font-size: 26px; line-height: 1.05; color: #ffffff;
  }
  .brand-dot { width: 14px; height: 14px; border-radius: 50%; background: #ffffff; flex: none; }

  .title-script {
    position: absolute; left: 650px; top: 612px; width: 230px; text-align: center;
    font-family: "Great Vibes", cursive; font-size: 72px; line-height: 1; color: #ffffff;
  }
  .title-rule { position: absolute; left: 616px; top: 708px; width: 262px; height: 1px; background: #d8d8d8; }
  .title-main {
    position: absolute; left: 614px; top: 712px; width: 266px; text-align: center;
    font-family: "Cinzel", serif; font-weight: 700; font-size: 66px; line-height: 1; color: #ffffff;
  }
</style>
</head>
<body>
<main class="flyer">
  <svg class="flyer-shapes" width="896" height="1160" viewBox="0 0 896 1160" aria-hidden="true">
    <rect x="0" y="0" width="299" height="1160" fill="#5f5f62"/>
    <path d="M0,110 C120,150 240,250 299,330 L299,960 C270,1040 240,1100 220,1160 L150,1160 C150,1050 120,960 60,900 L0,880 Z" fill="#0b0b0d"/>
    <rect x="299" y="0" width="298" height="1160" fill="#15151f"/>
    <rect x="597" y="0" width="299" height="1160" fill="#6a6a6d"/>
    <path d="M597,110 C700,160 820,280 896,440 L896,1090 C820,930 720,830 597,780 Z" fill="#15151f"/>
  </svg>

  <!-- Panel 1 -->
  <div class="section-label" style="left:136px;top:15px;">Corporate Magic</div>
  <div class="photo photo--warm" style="left:24px;top:76px;width:250px;height:250px;" role="img" aria-label="Photo of the magician performing for guests at a corporate banquet table"></div>
  <div class="copy" style="left:21px;top:348px;">
    <p class="lead">Magic at your corporate function adds an element that will distinguish your company from others.</p>
    <p>100_0580Whether it's performing at your trade show booth, working your hospitality Suite, Awards Banquet, or Company Picnic, Wesley has performed in all these venues and more from private businesses to top 100 corporations in the united states.</p>
    <p class="subhead">Close Up Performances</p>
    <p>Having a close up entertainer at your events brings the entertainment and amazement of watching an illusionist into a smaller venue, allowing the feeling of an intimate show for you and your guests to enjoy and create memories together. Perfect for audiences of 40 guests or less. This is live entertainment using no smoke and mirrors but pure sleight of hand. Perfect for holiday Parties, special events, hospitality suites, award dinners, and other smaller venues. Wesley has been performing his close up magic show for over 30 years, working from Southern California, Las Vegas, the Mid West, all the way to the Gulf Coast of Florida.</p>
  </div>
  <div class="section-label" style="left:0;top:746px;">Stage, Banquet, Palor Show</div>
  <div class="copy" style="left:21px;top:786px;">
    <p>This type of Magic show plays well for an audience of 10-5,000. This includes the skilled sleight of hand, comedy, and mentalism, using many volunteers from the audience, essentially bringing the audience up on stage, becoming part of the show.</p>
  </div>
  <div class="photo photo--warm" style="left:2px;top:925px;width:250px;height:250px;" role="img" aria-label="Photo of a guest watching a close-up rope trick at a banquet"></div>

  <!-- Panel 2 -->
  <div class="photo photo--mono" style="left:321px;top:86px;width:250px;height:250px;" role="img" aria-label="Black and white photo of the magician performing for a guest"></div>
  <div class="section-label" style="left:300px;top:375px;">About Wesley</div>
  <div class="copy" style="left:313px;top:415px;">
    <p>Why should you hire me? I have been performing magic since age 8, and have a love and passion for making people smile and laugh, but here are some other reasons.</p>
    <p><strong>I'm funny!</strong> You're guests will be laughing throughout the show guaranteeing a fun-filled experience!</p>
    <p><strong>I work clean.</strong> Yes, not only do I bathe every day, but all of my comedy is corporate clean. You won't hear any blue material in my show, and I won't embarrass anyone. You can rest assured that all of your guests will be treated with respect and look like stars.</p>
    <p><strong>No cheesy tricks here.</strong> Your guests will experience magic that looks like magic. Their jaws will drop and they will literally gasp in amazement making your event one they will remember for years to come.</p>
  </div>
  <div class="photo photo--warm-red" style="left:391px;top:700px;width:212px;height:212px;" role="img" aria-label="Photo of the magician performing close-up magic at a table with guests"></div>
  <div class="photo photo--warm" style="left:316px;top:954px;width:172px;height:172px;" role="img" aria-label="Photo of a guest reacting to a close-up trick"></div>

  <!-- Panel 3 -->
  <div class="brand"><span class="brand-dot"></span><span>Wesley Torvand Magic</span></div>
  <div class="hero-photo" role="img" aria-label="Photo of the magician in a dark suit and glasses performing on stage"></div>
  <div class="title-script">Magic</div>
  <div class="title-rule"></div>
  <div class="title-main">SHOWS</div>
  <div class="photo photo--stage" style="left:631px;top:876px;width:240px;height:240px;" role="img" aria-label="Photo of the magician performing a rope trick with a volunteer on stage"></div>
</main>
</body>
</html>
```